Design some Business Cards

Create a set of business cards for council of Marrowden.
The cards should be somehow indicative of the level/ status age group of the members, which i why a small description of the stages is included.
The card should look professional and colours and designs should match or complement the initial scheme.

```html
<!DOCTYPE html>
<html lang="en">
<head>
<meta charset="utf-8">
<title>Council of Marrowden — Business Cards</title>
<link href="https://fonts.googleapis.com/css2?family=Open+Sans:wght@400;600&display=swap" rel="stylesheet">
<style>
  :root {
    --backdrop: #2c2f34;
    --card-black: #121314;
    --sage: #3e5c55;
    --leaf: #7fa25c;
    --paper: #f2f2f2;
    --ink-light: #e8e8e8;
  }
  * { margin: 0; padding: 0; box-sizing: border-box; }
  html, body { width: 1200px; height: 900px; overflow: hidden; }
  body {
    background: var(--backdrop);
    font-family: "Open Sans", sans-serif;
    position: relative;
  }
  .card {
    position: absolute;
    left: 250px;
    width: 700px;
    height: 400px;
    background: var(--card-black);
    overflow: hidden;
    box-shadow: 0 10px 30px rgba(0,0,0,.45);
  }
  .card--back { top: 40px; }
  .card--front { top: 470px; }

  .brand {
    display: flex;
    align-items: center;
    gap: 12px;
    color: var(--leaf);
    font-weight: 600;
  }
  .brand__dot {
    width: 34px; height: 34px;
    border-radius: 50%;
    background: var(--leaf);
    flex: none;
  }
  .card--back .brand {
    position: absolute;
    top: 120px; left: 0; right: 0;
    justify-content: center;
    font-size: 30px;
  }
  .back-band {
    position: absolute;
    left: 0; bottom: 0;
    width: 700px; height: 112px;
  }
  .back-band__url {
    position: absolute;
    left: 0; right: 0; bottom: 40px;
    text-align: center;
    color: var(--ink-light);
    font-size: 16px;
    letter-spacing: .5px;
  }

  .front-shapes { position: absolute; inset: 0; }
  .front-info {
    position: absolute;
    top: 42px; left: 46px;
  }
  .card--front .brand { font-size: 24px; margin-bottom: 26px; }
  .person__name { color: var(--ink-light); font-size: 22px; font-weight: 600; }
  .person__role { color: var(--leaf); font-size: 13px; margin-bottom: 18px; }
  .contacts { list-style: none; }
  .contacts li {
    display: flex; align-items: center; gap: 10px;
    color: var(--ink-light);
    font-size: 14px;
    line-height: 1.35;
    margin-bottom: 8px;
  }
  .contacts svg { width: 18px; height: 18px; flex: none; }
  .contacts .address { align-items: flex-start; }
</style>
</head>
<body>

<section class="card card--back" aria-label="Card back">
  <div class="brand"><span class="brand__dot"></span>Council of Marrowden</div>
  <svg class="back-band" viewBox="0 0 700 112" aria-hidden="true">
    <polygon fill="var(--sage)" points="0,0 338,0 350,-14 362,0 700,0 700,112 0,112"/>
    <polygon fill="var(--sage)" points="338,1 350,-14 362,1"/>
  </svg>
  <svg style="position:absolute;left:336px;top:274px" width="28" height="16" aria-hidden="true">
    <polygon fill="var(--sage)" points="0,16 14,0 28,16"/>
  </svg>
  <div class="back-band__url">www.marrowdencouncil.org</div>
</section>

<section class="card card--front" aria-label="Card front">
  <svg class="front-shapes" viewBox="0 0 700 400" aria-hidden="true">
    <polygon fill="var(--sage)" points="400,400 700,400 700,0 580,0"/>
    <polygon fill="var(--paper)" points="470,400 610,400 700,120 700,60"/>
  </svg>
  <div class="front-info">
    <div class="brand"><span class="brand__dot"></span>Council of Marrowden</div>
    <p class="person__name">Your Name Here</p>
    <p class="person__role">President &amp; CEO</p>
    <ul class="contacts">
      <li>
        <svg viewBox="0 0 20 20"><circle cx="10" cy="10" r="9" fill="none" stroke="#e8e8e8" stroke-width="1.5"/><path d="M7 5.5l2 2-1 1.3c.6 1.4 1.8 2.6 3.2 3.2l1.3-1 2 2-1.2 1.5c-3.6-.4-6.9-3.7-7.3-7.3z" fill="#e8e8e8"/></svg>
        +44 1632 960 418
      </li>
      <li>
        <svg viewBox="0 0 20 20"><circle cx="10" cy="10" r="9" fill="none" stroke="#e8e8e8" stroke-width="1.5"/><rect x="5" y="6.5" width="10" height="7" fill="none" stroke="#e8e8e8" stroke-width="1.3"/><path d="M5 6.5l5 4 5-4" fill="none" stroke="#e8e8e8" stroke-width="1.3"/></svg>
        hello@marrowden.org
      </li>
      <li>
        <svg viewBox="0 0 20 20"><circle cx="10" cy="10" r="9" fill="none" stroke="#e8e8e8" stroke-width="1.5"/><ellipse cx="10" cy="10" rx="3.5" ry="9" fill="none" stroke="#e8e8e8" stroke-width="1.2"/><path d="M1 10h18" stroke="#e8e8e8" stroke-width="1.2"/></svg>
        www.marrowdencouncil.org
      </li>
      <li class="address">
        <svg viewBox="0 0 20 20"><path d="M10 1.5c-3.3 0-6 2.6-6 5.9 0 4.3 6 11.1 6 11.1s6-6.8 6-11.1c0-3.3-2.7-5.9-6-5.9z" fill="#e8e8e8"/><circle cx="10" cy="7.5" r="2.2" fill="var(--card-black)"/></svg>
        <span>14 Harrow Lane, Suite 3<br>Marrowden, MD4 7RL, UK</span>
      </li>
    </ul>
  </div>
</section>

</body>
</html>
```